Packaging and Logo for upscale skincare line

The name of the brand is Vivianne Vivianne. We would like a logo that's a mirror image of there name Vivianne. Packaging design for three signature products, face cream, body cream, and an aerosol spf. The face cream should be about 1/3 of the size of the body cream, in similarly shaped containers with twist-off lids, and a spatula for the face cream. And the spf should be a taller, slimmer, bottle with removable cap and aerosol spray.

Industry/Entity Type

Skin Care

Logo Text

Vivianne

Colors
2a71b2
3176b5
85acd3
ffffff

Requirements
Must have
Nice to have
• Would like the logo Vivianne Vivianne to be a single Vivianne in a mirror image. We also want the packaging to are in a deep blue ocean color with either a chrome or satin finish and the logo/wording on it to be almost like a pearl color. See colors attached.

```html
<!DOCTYPE html>
<html lang="en">
<head>
<meta charset="utf-8">
<title>Vivianne Skincare Packaging</title>
<link rel="stylesheet" href="https://fonts.googleapis.com/css2?family=Jost:wght@200;300;600&display=swap">
<style>
  :root {
    --canvas: #ffffff;
    --ocean: #1b2a8a;
    --ocean-deep: #16237a;
    --ocean-light: #2a3ca8;
    --pearl: #dfe3ee;
    --label-blue: #85acd3;
    --chrome-dark: #8a8f96;
    --chrome-light: #f4f5f7;
  }
  * { margin: 0; padding: 0; box-sizing: border-box; }
  html, body {
    width: 1200px; height: 1200px; overflow: hidden;
    background: var(--canvas);
    font-family: "Jost", sans-serif;
  }
  .canvas { position: relative; width: 1200px; height: 1200px; }

  .brand-name {
    position: absolute; left: 0; width: 100%; text-align: center;
    font-family: "Jost", sans-serif; font-weight: 200;
    color: var(--pearl); letter-spacing: 0.1em; line-height: 1;
    white-space: nowrap;
  }
  .product-name {
    position: absolute; left: 0; width: 100%; text-align: center;
    font-family: "Jost", sans-serif; font-weight: 600;
    color: var(--label-blue); line-height: 1; letter-spacing: 0.02em;
    white-space: nowrap;
  }
  .net-wt {
    position: absolute; left: 0; width: 100%; text-align: center;
    font-family: "Jost", sans-serif; font-weight: 300;
    color: var(--label-blue); line-height: 1;
    white-space: nowrap;
  }

  .label-panel {
    position: absolute; left: 169px; top: 209px; width: 416px; height: 337px;
    background: var(--ocean);
  }
  .label-panel .brand-name { font-size: 80px; }
  .label-panel .brand-upper { top: 65px; }
  .label-panel .product-name { top: 142px; font-size: 40px; }
  .label-panel .brand-lower { top: 174px; }

  .jar { position: absolute; }
  .jar-lid, .jar-base {
    position: absolute; left: 0; width: 100%;
    background: linear-gradient(90deg, var(--ocean-deep) 0%, var(--ocean-light) 22%, var(--ocean) 50%, var(--ocean-light) 78%, var(--ocean-deep) 100%);
  }
  .jar-lid { top: 0; border-radius: 6px 6px 2px 2px; }
  .jar-base { border-radius: 2px 2px 14px 14px; }

  .jar-small { left: 209px; top: 799px; width: 216px; height: 173px; }
  .jar-small .jar-lid { height: 68px; }
  .jar-small .jar-base { top: 70px; height: 103px; }
  .jar-small .brand-name { font-size: 26px; }
  .jar-small .brand-upper { top: 84px; }
  .jar-small .product-name { top: 111px; font-size: 13px; }
  .jar-small .brand-lower { top: 119px; }
  .jar-small .net-wt { top: 155px; font-size: 10px; }

  .jar-large { left: 461px; top: 662px; width: 388px; height: 316px; }
  .jar-large .jar-lid { height: 122px; }
  .jar-large .jar-base { top: 125px; height: 191px; }
  .jar-large .brand-name { font-size: 54px; }
  .jar-large .brand-upper { top: 154px; }
  .jar-large .product-name { top: 207px; font-size: 26px; }
  .jar-large .brand-lower { top: 222px; }
  .jar-large .net-wt { top: 291px; font-size: 13px; }

  .bottle { position: absolute; left: 879px; top: 428px; width: 130px; height: 544px; }
  .bottle-cap {
    position: absolute; left: 0; top: 0; width: 100%; height: 138px;
    border-radius: 6px 6px 0 0;
    background: linear-gradient(90deg, var(--chrome-dark) 0%, var(--chrome-light) 18%, #ffffff 40%, #3e4248 58%, var(--chrome-light) 78%, var(--chrome-dark) 100%);
  }
  .bottle-collar {
    position: absolute; left: 0; top: 138px; width: 100%; height: 18px;
    background: linear-gradient(180deg, #f1f2f4, #c9ccd2);
    font-family: "Jost", sans-serif; font-size: 10px; color: #9aa0a8;
    text-align: center; line-height: 18px; letter-spacing: 0.05em;
  }
  .bottle-body {
    position: absolute; left: 0; top: 156px; width: 100%; height: 388px;
    border-radius: 0 0 4px 4px;
    background: linear-gradient(90deg, var(--ocean-deep) 0%, var(--ocean-light) 25%, var(--ocean) 55%, var(--ocean-deep) 100%);
  }
  .bottle .brand-name { font-size: 25px; letter-spacing: 0.08em; }
  .bottle .brand-upper { top: 311px; }
  .bottle .product-name { top: 337px; font-size: 12px; }
  .bottle .brand-lower { top: 345px; }
  .bottle .net-wt { top: 512px; font-size: 10px; }
</style>
</head>
<body>
<main class="canvas">
  <section class="label-panel">
    <p class="brand-name brand-upper">vivianne</p>
    <p class="product-name">FACE CREM</p>
    <p class="brand-name brand-lower">vivianne</p>
  </section>

  <div class="jar jar-small">
    <div class="jar-lid"></div>
    <div class="jar-base"></div>
    <p class="brand-name brand-upper">vivianne</p>
    <p class="product-name">FACE CREM</p>
    <p class="brand-name brand-lower">vivianne</p>
    <p class="net-wt">NET WT (oz)</p>
  </div>

  <div class="jar jar-large">
    <div class="jar-lid"></div>
    <div class="jar-base"></div>
    <p class="brand-name brand-upper">vivianne</p>
    <p class="product-name">BODY CREAM</p>
    <p class="brand-name brand-lower">vivianne</p>
    <p class="net-wt">NET WT (oz)</p>
  </div>

  <div class="bottle">
    <div class="bottle-cap"></div>
    <div class="bottle-collar">SHOWROOM</div>
    <div class="bottle-body"></div>
    <p class="brand-name brand-upper">vivianne</p>
    <p class="product-name">AEROSOL SPF</p>
    <p class="brand-name brand-lower">vivianne</p>
    <p class="net-wt">NET WT (oz)</p>
  </div>
</main>
</body>
</html>
```